Three Self-help Book Covers for BRG

We need three book covers designed.

We have a good idea what the three designs will be and our directions are attached along with sample artwork.

1-Nine Quiet Lanterns
2-The PaperKite Almanac
3-The Driftwood

My schools website is: www.BrightmoorRiverGuild.example

Target Market(s)

Self-help

Industry/Entity Type

Life Coaching

Font styles to use
Other font styles liked:
• See Attachment for details

Requirements
Must have
• See Attached Suggestions
Nice to have
Should not have

```html
<!DOCTYPE html>
<html lang="en">
<head>
<meta charset="UTF-8">
<title>The PaperKite Almanac — Book Cover</title>
<link rel="stylesheet" href="https://fonts.googleapis.com/css2?family=Comic+Neue:wght@400;700&family=Open+Sans:wght@400;600;700&display=swap">
<style>
  :root {
    --backdrop-light: #e4e6e7;
    --backdrop-dark: #a9adaf;
    --mint-deep: #8cc5ad;
    --mint-mid: #9fd3bd;
    --mint-light: #b3e2cf;
    --ink: #1d2120;
    --photo-dark: #1b1210;
    --photo-warm: #8a4a32;
    --photo-glow: #c9785a;
  }
  * { box-sizing: border-box; margin: 0; padding: 0; }
  html, body {
    width: 1200px;
    height: 900px;
    overflow: hidden;
  }
  body {
    background: radial-gradient(ellipse at 50% 40%, var(--backdrop-light) 0%, var(--backdrop-dark) 100%);
    display: flex;
    align-items: center;
    justify-content: center;
  }
  .book-cover {
    width: 540px;
    height: 820px;
    display: flex;
    flex-direction: column;
    background: var(--mint-deep);
    box-shadow: 0 18px 40px rgba(0,0,0,0.25);
  }
  .title-band {
    height: 190px;
    background: linear-gradient(180deg, var(--mint-mid) 0%, var(--mint-deep) 100%);
    padding: 62px 0 0 56px;
    font-family: "Comic Neue", "Comic Sans MS", cursive;
    color: var(--ink);
  }
  .book-title {
    font-size: 40px;
    font-weight: 400;
    line-height: 1.05;
  }
  .book-subtitle {
    font-size: 25px;
    font-weight: 400;
    margin: 6px 0 0 26px;
  }
  .tagline-band {
    height: 78px;
    background: var(--mint-light);
    border-top: 2px solid rgba(255,255,255,0.45);
    display: flex;
    align-items: center;
    justify-content: center;
    text-align: center;
    font-family: "Open Sans", Calibri, sans-serif;
    font-size: 12.5px;
    line-height: 1.55;
    color: var(--ink);
  }
  .cover-photo {
    flex: 1;
    background:
      radial-gradient(ellipse at 48% 55%, var(--photo-glow) 0%, var(--photo-warm) 30%, transparent 65%),
      linear-gradient(160deg, var(--photo-dark) 0%, #3a2018 55%, var(--photo-dark) 100%);
  }
  .author-band {
    height: 92px;
    background: linear-gradient(180deg, var(--mint-mid) 0%, var(--mint-deep) 100%);
    display: flex;
    align-items: center;
    justify-content: center;
    font-family: "Open Sans", Calibri, sans-serif;
    font-weight: 700;
    font-size: 18px;
    color: var(--ink);
  }
</style>
</head>
<body>
  <main class="book-cover">
    <header class="title-band">
      <h1 class="book-title">The PaperKite Almanac</h1>
      <p class="book-subtitle">A Guide Book for the Inner You</p>
    </header>
    <section class="tagline-band">
      <p>Based on the Life Coaching Training Method that’s<br>Changing the world “one soul at a time” The KiteWay ™</p>
    </section>
    <div class="cover-photo" role="img" aria-label="Cupped hands holding dark stones engraved with the words Hope, Faith, Peace, Love and Believe"></div>
    <footer class="author-band">By Master Coach Lio Vantrell</footer>
  </main>
</body>
</html>
```